Dar Qamar Crossline Web Design

We need Simple but very Elegant Website for Our Middle East Company based in Kuwait, We are not good in describing design but we need simple but elegant and responsive to attract new market and to enable us competing in business

Industry/Entity Type

It Company

```html
<!DOCTYPE html>
<html lang="en">
<head>
<meta charset="utf-8">
<title>Dar Qamar Crossline</title>
<link rel="stylesheet" href="https://fonts.googleapis.com/css2?family=Source+Sans+Pro:ital,wght@0,400;0,600;0,700;1,400&family=Open+Sans:wght@400;600;700&family=Bungee+Outline&display=swap">
<style>
:root{
  --navy:#0f2133;
  --navy-deep:#0a1826;
  --red:#c8102e;
  --gold:#d4b300;
  --green:#2e9e2e;
  --blue:#1a8ad4;
  --ink:#333333;
  --muted:#777777;
  --soft:#f5f5f5;
  --line:#e4e4e4;
  --footer:#3a3a3a;
  --footer-base:#2b2b2b;
  --white:#ffffff;
}
*{margin:0;padding:0;box-sizing:border-box}
html,body{width:1200px;height:3175px;overflow:hidden}
body{position:relative;background:var(--white);font-family:"Open Sans",Arial,sans-serif;color:var(--ink)}
.abs{position:absolute}
.heading{font-family:"Source Sans Pro",Arial,sans-serif;font-weight:600;font-size:24px;color:var(--ink);text-align:center;width:1200px;left:0;letter-spacing:.3px}
.lead{font-size:12.5px;line-height:23px;color:var(--muted);text-align:center;left:300px;width:600px}

/* hero */
.hero{left:0;top:0;width:1200px;height:449px;background:linear-gradient(180deg,#1c2a5a 0%,#4b4a8f 30%,#a86a9c 48%,#2a3a6a 62%,#0c1836 100%)}
.nav{left:0;top:0;width:1200px;height:66px;background:rgba(6,14,34,.55)}
.brand{left:159px;top:18px;font-family:"Source Sans Pro",sans-serif;font-weight:700;font-size:21px;color:var(--white);letter-spacing:.5px}
.menu{right:163px;top:24px;display:flex;gap:24px;align-items:center}
.menu a{font-family:"Source Sans Pro",sans-serif;font-weight:700;font-size:13px;color:var(--white);text-decoration:none}
.burger{width:20px;height:12px;border-top:2px solid #fff;border-bottom:2px solid #fff;position:relative;margin-left:8px}
.burger::after{content:"";position:absolute;left:0;top:3px;width:20px;height:2px;background:#fff}
.hero-kicker{left:262px;top:190px;font-family:"Source Sans Pro",sans-serif;font-weight:700;font-size:19px;color:var(--white);letter-spacing:.5px}
.hero-title{left:158px;top:218px;font-family:"Bungee Outline",cursive;font-size:46px;color:var(--white);letter-spacing:1px}
.btn-enquire{left:269px;top:294px;width:213px;height:43px;background:var(--red);color:#fff;font-family:"Source Sans Pro",sans-serif;font-weight:700;font-size:16px;display:flex;align-items:center;justify-content:center}

/* about */
.intro-media{left:184px;top:667px;width:406px;height:281px;border-radius:10px 10px 4px 4px;background:linear-gradient(180deg,#2b2b2b 0%,#6aa3d8 8%,#b9d7ef 55%,#c9b08a 80%,#9a9a9a 92%,#d8d8d8 100%)}
.sub-title{font-family:"Source Sans Pro",sans-serif;font-weight:700;font-size:15px;color:var(--ink)}
.body-copy{font-size:11.5px;line-height:21px;color:#555}
.link-more{font-size:11.5px;color:var(--green)}

/* services */
.services{left:0;top:986px;width:1200px;height:368px;background:var(--soft);border-top:1px solid var(--line);border-bottom:1px solid var(--line)}
.service-photo{width:108px;height:105px;background:linear-gradient(135deg,#8a6b4e,#c9a27a 50%,#5b4a3a)}
.service-name{font-family:"Source Sans Pro",sans-serif;font-weight:700;font-size:14px;color:var(--ink)}

/* benefits */
.benefit{width:200px;text-align:center}
.benefit-icon{width:44px;height:72px;margin:0 auto;background:var(--blue);border-radius:22px 22px 8px 8px}
.benefit-name{margin-top:24px;font-family:"Source Sans Pro",sans-serif;font-weight:700;font-size:14px;color:var(--ink)}
.benefit-text{margin-top:8px;font-size:11.5px;line-height:21px;color:#666}

/* testimonials */
.testimonials{left:0;top:1756px;width:1200px;height:396px;background:linear-gradient(180deg,#16293d,#0f2133 60%,#13263a)}
.quote{left:220px;top:1862px;width:760px;text-align:center;font-family:"Source Sans Pro",sans-serif;font-style:italic;font-size:17.5px;line-height:27px;color:#e9eef3}
.quote-mark{font-family:Georgia,serif;font-size:40px;color:#7f8c99;vertical-align:-14px;line-height:0}
.avatar{left:558px;top:1962px;width:84px;height:84px;border-radius:50%;border:3px solid #fff;background:linear-gradient(180deg,#d9c6a8,#e9ddd0)}
.client{left:0;width:1200px;top:2060px;text-align:center;font-size:11px;color:#fff}
.dots{left:577px;top:2108px;display:flex;gap:7px}
.dots span{width:9px;height:9px;border-radius:50%;background:#6b7886}
.dots span.on{background:#fff}

/* blog */
.post{width:271px;text-align:center}
.post-photo{width:271px;height:185px}
.post-date{margin-top:20px;font-size:12px;color:var(--ink)}
.post-title{margin-top:10px;font-size:12.5px;font-weight:700;line-height:21px;color:var(--ink)}
.post-text{margin-top:9px;font-size:11.5px;line-height:22px;color:#777;padding:0 14px}
.btn-read{margin:10px auto 0;width:97px;height:25px;background:var(--gold);color:#fff;font-size:10px;font-weight:700;display:flex;align-items:center;justify-content:center}

/* newsletter */
.newsletter{left:0;top:2749px;width:1200px;height:190px;background:var(--navy)}
.field{height:30px;background:#fff;font-size:11.5px;color:#999;padding:7px 10px}
.btn-sub{left:736px;top:2871px;width:127px;height:30px;background:var(--red);color:#fff;font-size:11px;font-weight:700;display:flex;align-items:center;justify-content:center}

/* footer */
.footer{left:0;top:2939px;width:1200px;height:193px;background:var(--footer)}
.foot-head{font-family:"Source Sans Pro",sans-serif;font-weight:700;font-size:13px;color:#fff;letter-spacing:.5px}
.foot-list{font-size:11.5px;line-height:21px;color:#e6e6e6}
.foot-list b{color:#fff}
.socials{left:878px;top:2995px;display:flex;gap:10px}
.socials span{width:26px;height:26px;border-radius:50%;border:1.5px solid #fff}
.base{left:0;top:3132px;width:1200px;height:43px;background:var(--footer-base);color:#aaa;font-size:9.5px;display:flex;align-items:center;justify-content:center;letter-spacing:.5px}
</style>
</head>
<body>

<header class="abs hero" role="img" aria-label="Evening harbour skyline with towers and a traditional boat on the water"></header>
<nav class="abs nav"></nav>
<div class="abs brand">Dar Qamar Crossline</div>
<div class="abs menu">
  <a>MORE INFORMATION</a><a>CONTACT ME</a><a>OUR SERVICES</a><a>MORE CHOICES</a><span class="burger"></span>
</div>
<div class="abs hero-kicker">LOREM IPSUM DOLLAR</div>
<div class="abs hero-title">LOREM IPSUM SET</div>
<div class="abs btn-enquire">ENQUIRE NOW</div>

<section>
  <h2 class="abs heading" style="top:481px">ABOUT COMPANY</h2>
  <p class="abs body-copy" style="left:229px;top:521px;width:742px;text-align:center;font-size:12.5px;line-height:21px">Lorem Ipsum is simply dummy text of the printing and typesetting industry. Lorem Ipsum has been the industry's standard dummy text ever since the 1500s, when an unknown printer took a galley of type and scrambled it to make a type specimen book. It has survived not only five centuries, but also the leap into electronic typesetting, remaining essentially unchanged. It was popularised in the 1960s with the release of Linetype sheets containing Lorem Ipsum passages, and more recently with desktop publishing software like Folio Composer including versions of Lorem Ipsum.</p>
  <div class="abs intro-media" role="img" aria-label="Laptop showing a video still of the city towers by the sea"></div>
  <h3 class="abs sub-title" style="left:599px;top:669px">INRTRODUCTION</h3>
  <p class="abs body-copy" style="left:599px;top:700px;width:442px">Lorem Ipsum is simply dummy text of the printing and typesetting industry. Lorem Ipsum has been the industry's standard dummy text ever since the 1500s, when an unknown printer took a galley of type and scrambled it to make a type specimen book.</p>
  <p class="abs body-copy" style="left:599px;top:800px;width:442px">It has survived not only five centuries, but also the leap into electronic typesetting, remaining essentially unchanged.</p>
  <a class="abs link-more" style="left:599px;top:861px">Learn More About Us »</a>
</section>

<section class="abs services"></section>
<h2 class="abs heading" style="top:1042px">OUR SERVICES</h2>
<p class="abs lead" style="top:1079px">Lorem Ipsum is simply dummy text of the printing and typesetting industry. Lorem Ipsum has been the industry's standard dummy text ever since the 1500s,</p>
<div class="abs service-photo" style="left:159px;top:1177px" role="img" aria-label="Counsellor talking with a couple"></div>
<h3 class="abs service-name" style="left:286px;top:1177px">LOREM IPSUM</h3>
<p class="abs body-copy" style="left:286px;top:1198px;width:300px">Individual counseling can range from providing an understanding ear for the clients who need to talk through thoughts.</p>
<a class="abs link-more" style="left:286px;top:1267px;font-weight:700">Know More »</a>
<div class="abs service-photo" style="left:633px;top:1177px" role="img" aria-label="Smiling family sitting together"></div>
<h3 class="abs service-name" style="left:758px;top:1177px">LOREM IPSUM</h3>
<p class="abs body-copy" style="left:758px;top:1198px;width:290px">Individual counseling can range from providing an understanding ear for the clients who need to talk through thoughts.</p>
<a class="abs link-more" style="left:758px;top:1267px;font-weight:700">Know More »</a>

<section>
  <h2 class="abs heading" style="top:1378px">BENEFITS</h2>
  <p class="abs lead" style="top:1415px">Lorem Ipsum is simply dummy text of the printing and typesetting industry. Lorem Ipsum has been the industry's standard dummy text ever since the 1500s,</p>
  <div class="abs benefit" style="left:150px;top:1519px"><div class="benefit-icon" role="img" aria-label="Figure with raised arms icon"></div><div class="benefit-name">LOREM IPSUM</div><p class="benefit-text">Lorem Ipsum is simply dummy text of the printing and typesetting industry. Lorem Ipsum.</p></div>
  <div class="abs benefit" style="left:385px;top:1519px"><div class="benefit-icon" role="img" aria-label="Meditation pose icon"></div><div class="benefit-name">LOREM IPSUM</div><p class="benefit-text">Lorem Ipsum is simply dummy text of the printing and typesetting industry. Lorem Ipsum.</p></div>
  <div class="abs benefit" style="left:630px;top:1519px"><div class="benefit-icon" role="img" aria-label="Person in a circle icon"></div><div class="benefit-name">LOREM IPSUM</div><p class="benefit-text">Lorem Ipsum is simply dummy text of the printing and typesetting industry. Lorem Ipsum.</p></div>
  <div class="abs benefit" style="left:859px;top:1519px"><div class="benefit-icon" role="img" aria-label="Balancing pose icon"></div><div class="benefit-name">LOREM IPSUM</div><p class="benefit-text">Lorem Ipsum is simply dummy text of the printing and typesetting industry. Lorem Ipsum.</p></div>
</section>

<section class="abs testimonials" role="img" aria-label="Dim backdrop of a person in a hall"></section>
<h2 class="abs heading" style="top:1795px;color:#fff">CUSTOMER TESTIMONIALS</h2>
<p class="abs quote"><span class="quote-mark">“</span> Lorem Ipsum is simply dummy text of the printing and typesetting industry. Lorem Ipsum has been the industry's standard dummy text ever since the 1500s, when an unknown printer took a galley of type and scrambled it to make a type specimen book. <span class="quote-mark">”</span></p>
<div class="abs avatar" role="img" aria-label="Client portrait"></div>
<div class="abs client">Mira Salem, <b>Australia</b></div>
<div class="abs dots"><span class="on"></span><span></span><span></span></div>

<section>
  <h2 class="abs heading" style="top:2176px">NEW FROM THE BLOG</h2>
  <p class="abs lead" style="top:2211px">Lorem Ipsum is simply dummy text of the printing and typesetting industry. Lorem Ipsum has been the industry's standard dummy text ever since the 1500s,</p>
  <article class="abs post" style="left:159px;top:2287px">
    <div class="post-photo" role="img" aria-label="Women doing yoga outdoors" style="background:linear-gradient(180deg,#6fb3e0,#b9dcf0 50%,#d86aa8 75%,#7aa04a)"></div>
    <div class="post-date">09/09/15</div>
    <div class="post-title">Lorem Ipsum is simply dummy text of the printing and typesetting industry.</div>
    <p class="post-text">Lorem Ipsum is simply dummy text of the printing and typesetting industry. Lorem Ipsum has been the industry's standard dummy text ever since the 1500s,</p>
    <div class="btn-read">READ MORE</div>
  </article>
  <article class="abs post" style="left:463px;top:2287px">
    <div class="post-photo" role="img" aria-label="Speaker addressing a seated group" style="background:linear-gradient(180deg,#e8e8e8,#c9c4bd 50%,#f2f2f2)"></div>
    <div class="post-date">09/09/15</div>
    <div class="post-title">Lorem Ipsum is simply dummy text of the printing and typesetting industry.</div>
    <p class="post-text">Lorem Ipsum is simply dummy text of the printing and typesetting industry. Lorem Ipsum has been the industry's standard dummy text ever since the 1500s,</p>
    <div class="btn-read">READ MORE</div>
  </article>
  <article class="abs post" style="left:768px;top:2287px">
    <div class="post-photo" role="img" aria-label="Group meeting around a table" style="background:linear-gradient(135deg,#f1ede6,#c9b9a4 45%,#5b7fa8 70%,#e6e2dc)"></div>
    <div class="post-date">09/09/15</div>
    <div class="post-title">Lorem Ipsum is simply dummy text of the printing and typesetting industry.</div>
    <p class="post-text">Lorem Ipsum is simply dummy text of the printing and typesetting industry. Lorem Ipsum has been the industry's standard dummy text ever since the 1500s,</p>
    <div class="btn-read">READ MORE</div>
  </article>
</section>

<section class="abs newsletter"></section>
<h2 class="abs heading" style="top:2775px;color:#fff">NEWSLETTER + FREE EBOOK</h2>
<p class="abs lead" style="top:2811px;color:#6f7f90">Lorem Ipsum is simply dummy text of the printing and typesetting industry. Lorem Ipsum has been the industry's standard dummy text ever since the 1500s,</p>
<div class="abs field" style="left:370px;top:2871px;width:176px">Name</div>
<div class="abs field" style="left:554px;top:2871px;width:176px">Email</div>
<div class="abs btn-sub">YES, I WANT THIS</div>

<footer class="abs footer"></footer>
<h4 class="abs foot-head" style="left:161px;top:2961px">WORK WITH ME</h4>
<p class="abs foot-list" style="left:161px;top:2988px;width:240px"><b>Call</b> 123-555-0142 or<br><b>email us at</b> hello@darqamar.example<br>for a free 30-minute consultation or to<br><b>schedule an appointment.</b></p>
<h4 class="abs foot-head" style="left:493px;top:2961px">NAVIGATE</h4>
<p class="abs foot-list" style="left:493px;top:2988px">About Us<br>Our Services<br>More Information<br>More Choices<br>Contact Me</p>
<p class="abs foot-list" style="left:696px;top:2988px">Blog<br>Testimonials<br>Privacy Policy<br>Disclaimer</p>
<h4 class="abs foot-head" style="left:878px;top:2961px">SOCIAL MEDIA</h4>
<div class="abs socials"><span></span><span></span><span></span><span></span><span></span></div>
<div class="abs base">© COPYRIGHT 2015 DAR QAMAR CROSSLINE</div>

</body>
</html>
```